Banner 34"x81"

This is for a Pull Up Banner
I am supplying a sample of my logo and some of my art work for you to incorporate into an upright banner.
Please business name:LuellaRo OpenHarbor Psychotherapy
phone number: 583-214-9067 NOT THE ONE ON THE BUSINESS CARD

```html
<!DOCTYPE html>
<html lang="en">
<head>
<meta charset="utf-8">
<title>LuellaRo OpenHarbor Psychotherapy – Pull Up Banner</title>
<link rel="stylesheet" href="https://fonts.googleapis.com/css2?family=Fira+Sans:wght@400;500;700&family=Montserrat:wght@500&display=swap">
<style>
  :root {
    --page: #eef0f1;
    --panel: #dcdbdc;
    --navy: #1c3766;
    --cyan: #00aee0;
    --sky: #1d8ccc;
    --royal: #2a5db0;
    --white: #ffffff;
    --photo-dark: #2a1b18;
    --photo-blue: #2b56b8;
  }
  html, body {
    margin: 0;
    width: 1200px;
    height: 4137px;
    overflow: hidden;
    background: var(--page);
  }
  .banner {
    position: absolute;
    left: 50px;
    top: 759px;
    width: 1100px;
    height: 2619px;
    display: block;
    box-shadow: 0 20px 60px rgba(0,0,0,.25);
  }
  .tagline { font-family: "Fira Sans", sans-serif; font-weight: 400; fill: var(--navy); }
  .brand-name { font-family: "Fira Sans", sans-serif; font-weight: 700; fill: var(--navy); }
  .contact { font-family: "Montserrat", sans-serif; font-weight: 500; fill: var(--navy); }
  .phone-number { font-family: "Montserrat", sans-serif; font-weight: 500; fill: var(--navy); }
  .logo-text { font-family: "Fira Sans", sans-serif; font-weight: 500; fill: var(--white); }
</style>
</head>
<body>
<svg class="banner" viewBox="0 0 510 1214" xmlns="http://www.w3.org/2000/svg">
  <defs>
    <linearGradient id="portraitTone" x1="0" y1="0" x2="1" y2="1">
      <stop offset="0" stop-color="#3a2420"/>
      <stop offset="0.45" stop-color="#2a1b18"/>
      <stop offset="0.7" stop-color="#2b56b8"/>
      <stop offset="1" stop-color="#1b1412"/>
    </linearGradient>
    <linearGradient id="cyanBand" x1="0" y1="0" x2="1" y2="0">
      <stop offset="0" stop-color="var(--cyan)"/>
      <stop offset="1" stop-color="var(--sky)"/>
    </linearGradient>
  </defs>

  <!-- panel -->
  <rect class="panel" width="510" height="1214" fill="var(--panel)"/>

  <!-- portrait area -->
  <g role="img" aria-label="Portrait photograph of the therapist seated in a dark leather chair, wearing a blue sweater">
    <polygon points="0,0 510,0 510,470 0,702" fill="url(#portraitTone)"/>
  </g>

  <!-- top-left corner accent -->
  <g class="corner-accent">
    <polygon points="0,0 260,0 0,165" fill="var(--navy)"/>
    <polygon points="0,170 112,100 112,128 0,190" fill="var(--sky)"/>
    <polygon points="0,162 50,131 50,146 0,177" fill="var(--white)"/>
  </g>

  <!-- logo -->
  <g class="logo">
    <rect x="372" y="35" width="108" height="87" fill="var(--royal)"/>
    <text class="logo-text" x="426" y="96" font-size="48" text-anchor="middle">LR</text>
  </g>

  <!-- diagonal bands -->
  <g class="diagonal-bands">
    <polygon points="47,733 63,645 385,522 372,606" fill="url(#cyanBand)"/>
    <polygon points="250,625 272,555 510,468 510,528" fill="var(--navy)"/>
    <polygon points="330,592 338,570 510,505 510,527" fill="var(--white)"/>
  </g>

  <!-- phone -->
  <g class="phone">
    <circle cx="398" cy="640" r="13" fill="var(--navy)"/>
    <path d="M392.5 633.5 l3 -1 l2 4.5 l-2 1.5 q1.5 3.5 5 5 l1.5 -2 l4.5 2 l-1 3 q-1 1.5 -3 1 q-8 -2.5 -11 -11 q-0.5 -2 1 -3z" fill="var(--white)"/>
    <text class="phone-number" x="398" y="685" font-size="27" text-anchor="middle">583-214-9067</text>
  </g>

  <!-- business name -->
  <g class="business-name">
    <text class="tagline" x="255" y="757" font-size="23" text-anchor="middle">OpenHarbor</text>
    <text class="brand-name" x="255" y="822" font-size="58" text-anchor="middle">LuellaRo</text>
    <text class="tagline" x="255" y="858" font-size="27" text-anchor="middle">Psychotherapy</text>
  </g>

  <!-- contacts -->
  <g class="contacts">
    <circle cx="45" cy="915" r="10" fill="var(--navy)"/>
    <text class="contact" x="67" y="922" font-size="19">@LuellaHarbor</text>

    <circle cx="45" cy="955" r="10" fill="var(--navy)"/>
    <text class="contact" x="67" y="962" font-size="19">@LuellaOpenHarbor</text>

    <circle cx="45" cy="995" r="10" fill="var(--navy)"/>
    <rect x="39.5" y="991" width="11" height="8" rx="1" fill="var(--white)"/>
    <path d="M39.5 991.5 l5.5 4 l5.5 -4" fill="none" stroke="var(--navy)" stroke-width="1.2"/>
    <text class="contact" x="67" y="1002" font-size="19">LuellaOpenHarbor@harbormail.net</text>
  </g>

  <!-- footer bands -->
  <g class="footer-bands">
    <rect x="0" y="1140" width="510" height="74" fill="url(#cyanBand)"/>
    <polygon points="175,1198 230,1103 510,1103 510,1198" fill="var(--navy)"/>
    <polygon points="280,1130 306,1106 510,1106 510,1130" fill="var(--white)"/>
  </g>
</svg>
</body>
</html>
```